■書籍タイトル
「町工房・路地の店・士業のための、明日効く集客設計術・KRT」

・堅苦しくなく、わかりやすいイメージにしたいです
・電子書籍なので、画像が小さいので、できるだけ視認しやすい文字でお願いします

■オビ
「お金も時間もかけずに、たった2つのことをするだけで、ライバルが歯ぎしりするほどお客に選ばれる」

■著者  森野沙知絵
■発行  東陽商務文化出版舎

■色の指定などはありません。お任せです。
(明るい・カンタン・わかりやすい)
イメージイラストなど入ってもよいかと思います。

■高級感やアカデミックより、明るくカンタンなイメージで。

※参考資料として、書籍の原稿と、同じタイトルのセミナーのパワポ表紙画像を添付します。
アカデミックな感じより、ポップな感じや明るいイメージ、
「わかりやすさ」「文字の視認性」を重視します。
クラフターのみなさま、
引き続き、ご提案をお待ちしております。
みなさま、ご提案ありがとうございます。

中小企業・小さなお店・先生業
という文字が小さい表示のデザインが多いのですが、

ターゲット層が一目で見てわかるよう、

中小企業・小さなお店・先生業

という文字が見えるようにしたいです。

引き続き、みなさまからのご提案をお待ちしております。
たくさんのご提案をいただきありがとうございます。

本のタイトルが、変更となりました。
金額をアップし、締め切りを1日延長いたしますので、
訂正ご対応いただければ幸いです。

新しいタイトルは、

「中小企業・小さなお店・先生業が
常連が増え続けるために明日から始める三つの習慣」
です。

帯、またはサブタイトルは、
「ライバルが歯ぎしりするほどお客が押し寄せる新時代の差別化戦略」
としてください。

ご提案をお待ちしております。
よろしくお願いいたします。

今回の装丁は、特に「わかりやすさ」を重視しておりました。
レベルの高い装丁デザインが多く、選考に大変迷いました。
選定させていただきましたデザインは、笑顔の3職種の人物のイラストと、フォントの使い方など、わかりやすい・明るい・カンタンという目指すところをこちらの想定以上に表現していただいたことが一番の理由です。

たくさんのご提案をいただき、ありがとうございました。
本当にレベルの高いデザインが多く選定では社内でも意見が割れました。
また、再三の追記・変更によりお手数をおかけしましたことを、この場を借りてお詫び申し上げます。

今後も定期的に装丁の依頼をいたしますので、どうぞよろしくお願いいたします。

```html
<!DOCTYPE html>
<html lang="ja">
<head>
<meta charset="UTF-8">
<title>明日効く集客設計術 KRT</title>
<link href="https://fonts.googleapis.com/css2?family=M+PLUS+Rounded+1c:wght@500;800;900&display=swap" rel="stylesheet">
<style>
  :root {
    --sky: #3ea4f2;
    --paper: #ffffff;
    --ink: #111111;
    --lemon: #fdf27a;
  }
  html, body {
    margin: 0;
    padding: 0;
    overflow: hidden;
  }
  .cover {
    position: relative;
    width: 753px;
    height: 1200px;
    background: var(--sky);
    overflow: hidden;
    font-family: "M PLUS Rounded 1c", sans-serif;
    color: var(--ink);
  }
  .cover-shapes {
    position: absolute;
    inset: 0;
  }
  .audience {
    position: absolute;
    top: 28px;
    left: 455px;
    width: 270px;
    margin: 0;
    font-size: 33px;
    font-weight: 500;
    line-height: 1.5;
    letter-spacing: 0.02em;
  }
  .title {
    position: absolute;
    left: 76px;
    top: 300px;
    width: 600px;
    margin: 0;
    text-align: center;
    font-weight: 900;
    font-size: 84px;
    line-height: 1.36;
    letter-spacing: 0.06em;
    transform: rotate(12deg);
  }
  .title .line { display: block; }
  .obi {
    position: absolute;
    left: 0;
    top: 892px;
    width: 753px;
    height: 308px;
    background: var(--lemon);
  }
  .obi-copy {
    margin: 0;
    padding: 22px 20px 0 26px;
    font-size: 41px;
    font-weight: 500;
    line-height: 1.52;
    letter-spacing: 0.03em;
  }
  .obi-copy .line { display: block; white-space: nowrap; }
</style>
</head>
<body>
<div class="cover">
  <svg class="cover-shapes" width="753" height="1200" viewBox="0 0 753 1200" aria-hidden="true">
    <polygon points="0,220 170,150 170,182 0,262" fill="var(--paper)"/>
    <g class="cloud" fill="var(--paper)">
      <circle cx="430" cy="70" r="95"/>
      <circle cx="560" cy="40" r="110"/>
      <circle cx="690" cy="60" r="110"/>
      <circle cx="470" cy="170" r="70"/>
      <circle cx="590" cy="185" r="75"/>
      <circle cx="700" cy="170" r="70"/>
      <rect x="430" y="0" width="323" height="190"/>
    </g>
    <ellipse cx="378" cy="515" rx="355" ry="255" transform="rotate(12 378 515)"
             fill="var(--paper)" stroke="var(--ink)" stroke-width="7"/>
  </svg>

  <p class="audience">町工房・路地<br>の店・士業の<br>ための</p>

  <h1 class="title">
    <span class="line">明日効く</span>
    <span class="line">集客設計術</span>
    <span class="line">KRT</span>
  </h1>

  <div class="obi">
    <p class="obi-copy">
      <span class="line">お金も時間もかけずに、たった</span>
      <span class="line">2つのことをするだけで、ライ</span>
      <span class="line">バルが歯ぎしりするほどお客に</span>
      <span class="line">選ばれる</span>
    </p>
  </div>
</div>
</body>
</html>
```